Bright, Fun and hard to forget home inspection business card.

We need a Business card design for a new Home Inspection company. We are building a brand that is bright, fun and easy to remember.

Target Market(s)

Anyone involed in buying and selling of homes.

Industry/Entity Type

Home Inspection

Contact Information for Business Card

Colin Marlowe Owner/Inspector

Wedsite- PorchAndRafterCheck.example
Phone: 253-555-0187
Email- ColinMarlowe@mailbox.example
WA Lic # 4806

Requirements
Must have
• BRQV LOGO somewhere on card.

```html
<!DOCTYPE html>
<html lang="en">
<head>
<meta charset="utf-8">
<title>Porch And Rafter Check – Business Card</title>
<link rel="stylesheet" href="https://fonts.googleapis.com/css2?family=Open+Sans:wght@400;600;700&display=swap">
<style>
  :root {
    --stage: #e9e6e3;
    --card-dark: #1e1b1b;
    --card-light: #fbfbfa;
    --accent: #d9531e;
    --accent-soft: #e8774a;
    --ink: #1a1a1a;
    --muted: #4a4a4a;
    --ghost: rgba(255,255,255,0.05);
    --ghost-dark: rgba(0,0,0,0.05);
  }
  * { margin: 0; padding: 0; box-sizing: border-box; }
  html, body {
    width: 1200px; height: 768px; overflow: hidden;
    background: var(--stage);
    font-family: "Open Sans", Arial, sans-serif;
  }
  .stage { position: relative; width: 1200px; height: 768px; }
  .card {
    position: absolute; top: 229px;
    width: 540px; height: 310px;
    overflow: hidden;
    box-shadow: 0 6px 18px rgba(0,0,0,0.18);
  }

  /* Front */
  .card-front { left: 40px; background: var(--card-dark); }
  .front-ghost {
    position: absolute; right: 20px; top: 10px; width: 260px; height: 290px;
    border-radius: 50%;
    background: radial-gradient(ellipse at center, var(--ghost), transparent 70%);
  }
  .brand {
    position: absolute; left: 60px; top: 78px;
    display: flex; align-items: center; gap: 16px;
  }
  .brand-dot {
    width: 64px; height: 64px; border-radius: 50%;
    background: var(--accent); flex: none;
  }
  .brand-name {
    color: #ffffff; font-weight: 700; font-size: 28px; line-height: 1.08;
    text-transform: uppercase; letter-spacing: 0.5px;
  }
  .brand-name span { display: block; }
  .brand-name .brand-suffix { font-size: 13px; letter-spacing: 3px; margin-top: 4px; }

  /* Back */
  .card-back { left: 620px; background: var(--card-light); }
  .back-ghost {
    position: absolute; right: 10px; top: 40px; width: 260px; height: 260px;
    border-radius: 50%;
    background: radial-gradient(circle, var(--ghost-dark), transparent 70%);
  }
  .mascot-area {
    position: absolute; left: 0; top: 0; width: 250px; height: 310px;
    border-radius: 0 0 90px 0;
    background: linear-gradient(135deg, var(--accent) 0%, var(--accent-soft) 100%);
  }
  .badge {
    position: absolute; left: 150px; top: 224px;
    width: 60px; height: 66px; background: #2a2a2a; border-radius: 3px;
  }
  .person { position: absolute; right: 28px; top: 118px; text-align: right; }
  .person-name { color: var(--accent); font-weight: 700; font-size: 17px; }
  .person-role { color: var(--muted); font-size: 10px; margin-top: 4px; }
  .contact {
    position: absolute; right: 24px; bottom: 30px;
    list-style: none; text-align: right;
  }
  .contact li {
    display: flex; align-items: center; justify-content: flex-end; gap: 8px;
    color: var(--ink); font-size: 13px; line-height: 19px;
  }
  .contact svg { width: 11px; height: 11px; fill: var(--accent); flex: none; }
</style>
</head>
<body>
<main class="stage">
  <section class="card card-front">
    <div class="front-ghost" role="img" aria-label="Faint oversized mascot decoration"></div>
    <div class="brand">
      <span class="brand-dot"></span>
      <p class="brand-name">
        <span>Porch And</span>
        <span>Rafter</span>
        <span>Check</span>
        <span class="brand-suffix">LLC</span>
      </p>
    </div>
  </section>

  <section class="card card-back">
    <div class="back-ghost" role="img" aria-label="Faint oversized mascot decoration"></div>
    <div class="mascot-area" role="img" aria-label="Illustration of the inspector mascot holding a megaphone"></div>
    <div class="badge" role="img" aria-label="Certification badge"></div>
    <div class="person">
      <p class="person-name">Colin Marlowe</p>
      <p class="person-role">Owner/Inspector</p>
    </div>
    <ul class="contact">
      <li>WA Lic # 4806 <svg viewBox="0 0 12 12"><path d="M6 0a4 4 0 0 0-4 4c0 3 4 8 4 8s4-5 4-8a4 4 0 0 0-4-4zm0 5.5A1.5 1.5 0 1 1 6 2.5a1.5 1.5 0 0 1 0 3z"/></svg></li>
      <li>253-555-0187 <svg viewBox="0 0 12 12"><path d="M2 1h2l1 3-1.5 1a7 7 0 0 0 3.5 3.5L8 7l3 1v2a1 1 0 0 1-1 1C5 11 1 7 1 2a1 1 0 0 1 1-1z"/></svg></li>
      <li>ColinMarlowe@mailbox.example <svg viewBox="0 0 12 12"><path d="M0 2h12v8H0zM1 3l5 4 5-4"/></svg></li>
      <li>PorchAndRafterCheck.example <svg viewBox="0 0 12 12"><circle cx="6" cy="6" r="6"/></svg></li>
    </ul>
  </section>
</main>
</body>
</html>
```